Company Website for Zorvel Analytics, an open source data analytics company focused on relationship and li

I need a company/brand website for our new startup, Zorvel Analytics LLC. We are a company focused on using life pattern analysis techniques, looking at relationships and how relationships, attributes, and activity cluster to infer aggregate information about individuals and groups. Our focus is on improving the digital advertising market.

We have a company logo which I will upload shortly.

Target Market(s)

Digital Advertising

Number of Pages Required

3 page

Font styles to use
Sans Serif

Requirements
Must have
• An main page, about us, contact page.
Nice to have
• Zorvel Analytics relies on state of the art analytics applied to a the digital marketing space. While it is heavy in science, we also understand the art of influence. The website should have a scientific edge but also a flair that illustrates our focus on applying the hard science and analytics to influencing the behavior of people.

```html
<!DOCTYPE html>
<html lang="en">
<head>
<meta charset="utf-8">
<title>Zorvel Analytics</title>
<link href="https://fonts.googleapis.com/css2?family=Poppins:wght@400;500;600&family=Lato:wght@400;700&display=swap" rel="stylesheet">
<style>
:root{
  --blue:#1e6fbf;
  --blue-dark:#1a5fa6;
  --orange:#f7931e;
  --text:#666;
  --heading:#222;
  --grey-bg:#f5f5f5;
  --line:#d9d9d9;
}
*{box-sizing:border-box;margin:0;padding:0}
html,body{width:1200px;height:3169px;overflow:hidden}
body{font-family:'Lato',sans-serif;color:var(--text);background:#fff;position:relative}
.abs{position:absolute}
section,header,footer,.topbar{position:absolute;left:0;width:1200px}
.title{font-family:'Poppins',sans-serif;font-weight:600;font-size:32px;color:var(--blue);text-align:center;position:absolute;left:0;width:1200px}
.title span{color:var(--orange)}
.btn{position:absolute;background:var(--orange);color:#fff;font-family:'Poppins',sans-serif;font-weight:500;font-size:15px;display:flex;align-items:center;justify-content:center}

/* top bar */
.topbar{top:0;height:42px;background:var(--blue);color:#fff;font-size:15px}
.topbar .item{position:absolute;top:11px;display:flex;align-items:center;gap:12px}
.social{position:absolute;display:flex;gap:18px}
.social i{display:block;width:12px;height:12px;border-radius:50%;background:currentColor}

/* header */
header{top:42px;height:93px;background:#fff}
.brand{position:absolute;left:76px;top:32px;font-family:'Poppins',sans-serif;font-weight:600;font-size:24px;color:var(--blue);display:flex;align-items:center;gap:8px}
.brand b{width:12px;height:12px;border-radius:50%;background:var(--orange)}
.nav a{position:absolute;top:36px;font-family:'Poppins',sans-serif;font-size:14px;color:#555;text-decoration:none}
.nav a.active{color:var(--blue);font-weight:500}
.nav a.active::after{content:"";position:absolute;left:50%;margin-left:-6px;top:26px;width:12px;height:3px;background:var(--blue)}
.login{position:absolute;left:1018px;top:25px;width:104px;height:42px;border-radius:21px;background:var(--blue);color:#fff;font-family:'Poppins',sans-serif;font-weight:500;font-size:15px;display:flex;align-items:center;justify-content:center}

/* hero */
.hero{top:135px;height:573px;background:linear-gradient(120deg,#3a3a3a,#7b7066 40%,#4b4540 70%,#2a2a2a)}
.hero h1{position:absolute;top:190px;left:0;width:1200px;text-align:center;color:#fff;font-family:'Poppins',sans-serif;font-weight:600;font-size:28px;line-height:38px}
.hero p{position:absolute;top:300px;left:0;width:1200px;text-align:center;color:#fff;font-size:15px;line-height:26px}
.hero .btn{left:528px;top:387px;width:144px;height:40px}
.arrow{position:absolute;top:272px}

/* focus */
.focus{top:708px;height:501px;background:#fff}
.focus .title{top:58px}
.focus .intro{position:absolute;top:134px;left:280px;width:640px;text-align:center;font-size:14px;line-height:28px}
.feature{position:absolute;top:220px;width:240px;text-align:center}
.feature svg{display:block;margin:0 auto}
.feature .dash{width:12px;height:3px;background:var(--blue);margin:22px auto 0}
.feature h3{font-family:'Poppins',sans-serif;font-weight:500;font-size:16px;color:var(--heading);margin-top:22px}
.feature p{font-size:14px;line-height:28px;margin-top:6px}

/* about */
.about{top:1209px;height:429px;background:var(--grey-bg)}
.about .device{position:absolute;left:80px;top:59px;width:427px;height:306px;border-radius:14px;background:linear-gradient(135deg,#2d2d2d,#5a5a5a)}
.about h2{position:absolute;left:613px;top:60px;font-family:'Poppins',sans-serif;font-weight:600;font-size:32px;color:var(--blue)}
.about h2 span{color:var(--orange)}
.about p{position:absolute;left:613px;width:460px;font-size:14px;line-height:26px}
.about .btn{left:613px;top:323px;width:144px;height:40px}

/* news */
.news{top:1638px;height:437px;background:#fff}
.news .title{top:58px}
.card{position:absolute}
.card.side{top:145px;width:322px;height:207px}
.card.main{top:124px;left:440px;width:321px;height:249px;background:var(--blue)}
.card.main .img{height:146px;background:linear-gradient(135deg,#6a6f78,#b9b2aa)}
.card.main h4{color:#fff;font-family:'Poppins',sans-serif;font-weight:500;font-size:15px;line-height:26px;padding:10px 14px 0}
.meta{position:absolute;left:14px;bottom:12px;display:flex;gap:22px;color:#fff;font-size:12px;align-items:center}
.meta span{display:flex;gap:7px;align-items:center}

/* testimonial */
.testi{top:2075px;height:355px;background:var(--grey-bg)}
.testi .title{top:58px}
.avatar{position:absolute;left:211px;top:133px;width:106px;height:106px;border-radius:50%;background:radial-gradient(circle at 50% 40%,#c9d6e6,#1e6fbf)}
.testi p{position:absolute;left:363px;top:138px;width:652px;font-size:14px;line-height:26px}
.testi .who{position:absolute;left:363px;top:229px;color:var(--blue);font-family:'Poppins',sans-serif;font-weight:500;font-size:14px}
.dots{position:absolute;top:278px;left:553px;display:flex;gap:10px}
.dots i{width:10px;height:10px;border-radius:50%;border:1px solid #aaa}
.dots i.on{background:var(--blue);border-color:var(--blue)}

/* contact */
.contact{top:2430px;height:427px;background:#fff}
.contact .title{top:58px}
.field{position:absolute;width:364px;height:34px;border-bottom:1px solid var(--line);font-size:13px;color:#888}
.field.on{border-bottom-color:var(--blue);color:var(--blue)}
.contact .btn{left:528px;top:321px;width:144px;height:40px}

/* footer */
footer{top:2857px;height:312px;background:var(--blue);color:#fff;font-size:14px}
footer h5{position:absolute;top:48px;color:var(--orange);font-family:'Poppins',sans-serif;font-weight:500;font-size:14px}
footer .link{position:absolute;left:80px}
.contact-line{position:absolute;left:349px;display:flex;gap:14px;line-height:26px}
.fbrand{position:absolute;left:902px;top:70px;width:220px;text-align:center;font-family:'Poppins',sans-serif;font-weight:600;font-size:22px}
.rule{position:absolute;left:80px;top:249px;width:1042px;height:1px;background:rgba(255,255,255,.35)}
.copy{position:absolute;left:80px;top:271px;font-size:13px}
.copy span{color:var(--orange)}
</style>
</head>
<body>

<div class="topbar">
  <div class="item" style="left:78px">
    <svg width="16" height="16" viewBox="0 0 24 24" fill="#fff"><path d="M6.6 10.8a15 15 0 0 0 6.6 6.6l2.2-2.2c.3-.3.7-.4 1-.2 1.1.4 2.3.6 3.6.6.6 0 1 .4 1 1V20c0 .6-.4 1-1 1A17 17 0 0 1 3 4c0-.6.4-1 1-1h3.5c.6 0 1 .4 1 1 0 1.3.2 2.5.6 3.6.1.3 0 .7-.2 1z"/></svg>
    123 456 7890
  </div>
  <div class="item" style="left:254px">
    <svg width="18" height="14" viewBox="0 0 18 14"><rect x="0.5" y="0.5" width="17" height="13" fill="#fff"/><path d="M1 1l8 6 8-6" stroke="#1e6fbf" stroke-width="1.4" fill="none"/></svg>
    info@zorvelanalytics.com
  </div>
  <div class="social" style="left:1040px;top:15px;color:#fff"><i></i><i></i><i></i></div>
</div>

<header>
  <div class="brand"><b></b>Zorvel Analytics</div>
  <nav class="nav">
    <a class="active" style="left:688px">Home</a>
    <a style="left:787px">About Us</a>
    <a style="left:898px">Contact Us</a>
  </nav>
  <div class="login">Log in</div>
</header>

<section class="hero" role="img" aria-label="Photo of a business team smiling around a meeting table">
  <h1>Improving the digital advertising<br>market</h1>
  <p>Lorem Ipsum is simply dummy text of the printing<br>and typesetting industry.</p>
  <div class="btn">Contact Now</div>
  <svg class="arrow" style="left:32px" width="14" height="22" viewBox="0 0 14 22"><path d="M11 2L3 11l8 9" stroke="#bbb" stroke-width="2.5" fill="none"/></svg>
  <svg class="arrow" style="left:1154px" width="14" height="22" viewBox="0 0 14 22"><path d="M3 2l8 9-8 9" stroke="#fff" stroke-width="2.5" fill="none"/></svg>
</section>

<section class="focus">
  <h2 class="title">Company <span>Focus</span></h2>
  <p class="intro">Lorem Ipsum is simply dummy text of the printing and typesetting industry. Lorem Ipsum has been the industry's standard dummy text ever since the 1500s,</p>

  <div class="feature" style="left:74px">
    <svg width="90" height="90" viewBox="0 0 90 90"><circle cx="45" cy="45" r="30" fill="#eaf2fb"/><path d="M45 5a40 40 0 0 1 28 68" stroke="#1e6fbf" stroke-width="4" fill="none"/><path d="M5 45a40 40 0 0 1 30-39" stroke="#1e6fbf" stroke-width="4" fill="none"/><circle cx="40" cy="42" r="4" fill="#1e6fbf"/><circle cx="52" cy="42" r="4" fill="#1e6fbf"/><path d="M33 54c0-5 14-5 14 0M45 54c0-5 14-5 14 0" stroke="#1e6fbf" stroke-width="2" fill="none"/></svg>
    <div class="dash"></div><h3>Techniques</h3>
    <p>Lorem Ipsum is simply dummy<br>typesetting industry.</p>
  </div>
  <div class="feature" style="left:343px">
    <svg width="90" height="90" viewBox="0 0 90 90"><circle cx="45" cy="45" r="30" fill="#1e6fbf"/><path d="M45 5a40 40 0 0 1 28 68" stroke="#1e6fbf" stroke-width="4" fill="none"/><path d="M5 45a40 40 0 0 1 30-39" stroke="#1e6fbf" stroke-width="4" fill="none"/><path d="M45 58L32 45a7 7 0 0 1 13-9 7 7 0 0 1 13 9z" fill="#fff"/></svg>
    <div class="dash"></div><h3>Relationships</h3>
    <p>Lorem Ipsum is simply dummy<br>typesetting industry.</p>
  </div>
  <div class="feature" style="left:613px">
    <svg width="90" height="90" viewBox="0 0 90 90"><circle cx="45" cy="45" r="30" fill="#eaf2fb"/><path d="M45 5a40 40 0 0 1 28 68" stroke="#1e6fbf" stroke-width="4" fill="none"/><path d="M5 45a40 40 0 0 1 30-39" stroke="#1e6fbf" stroke-width="4" fill="none"/><path d="M40 34v22m-4-4l4 4 4-4M48 36h8M48 44h6M48 52h4" stroke="#1e6fbf" stroke-width="2.4" fill="none"/></svg>
    <div class="dash"></div><h3>Attributes</h3>
    <p>Lorem Ipsum is simply dummy<br>typesetting industry.</p>
  </div>
  <div class="feature" style="left:886px">
    <svg width="90" height="90" viewBox="0 0 90 90"><circle cx="45" cy="45" r="30" fill="#eaf2fb"/><path d="M45 5a40 40 0 0 1 28 68" stroke="#1e6fbf" stroke-width="4" fill="none"/><path d="M5 45a40 40 0 0 1 30-39" stroke="#1e6fbf" stroke-width="4" fill="none"/><g fill="#1e6fbf"><circle cx="45" cy="45" r="3"/><circle cx="36" cy="36" r="3"/><circle cx="54" cy="36" r="3"/><circle cx="36" cy="54" r="3"/><circle cx="54" cy="54" r="3"/></g><path d="M36 36l18 18M54 36L36 54" stroke="#1e6fbf" stroke-width="1.5"/></svg>
    <div class="dash"></div><h3>Activity Cluster</h3>
    <p>Lorem Ipsum is simply dummy<br>typesetting industry.</p>
  </div>
</section>

<section class="about">
  <div class="device" role="img" aria-label="Tablet showing the website home page"></div>
  <h2>About <span>Us</span></h2>
  <p style="top:134px">Lorem Ipsum is simply dummy text of the printing and typesetting industry. Lorem Ipsum has been the industry's standard dummy</p>
  <p style="top:212px">1500s, when an unknown printer took a galley of type and scrambled it to make a type specimen book. It has but also the leap into electronic typesetting, remaining essentially unchanged.</p>
  <div class="btn">Read More</div>
</section>

<section class="news">
  <h2 class="title">Recent <span>News</span></h2>
  <div class="card side" style="left:78px;background:linear-gradient(135deg,#3b2a2a,#8a6d62 60%,#2f2f35)" role="img" aria-label="Photo of a woman working on a laptop"></div>
  <div class="card main">
    <div class="img" role="img" aria-label="Photo of colleagues reviewing work at a desk"></div>
    <h4>Lorem Ipsum is simply dummy<br>text of typesetting</h4>
    <div class="meta">
      <span><svg width="13" height="12" viewBox="0 0 24 22"><path d="M12 21L2 11a6 6 0 0 1 10-8 6 6 0 0 1 10 8z" fill="#fff"/></svg>Likes</span>
      <span><svg width="14" height="12" viewBox="0 0 24 20"><path d="M2 2h20v12H9l-5 4v-4H2z" fill="none" stroke="#fff" stroke-width="2.4"/></svg>Comments</span>
      <span><svg width="12" height="12" viewBox="0 0 20 20"><rect x="2" y="4" width="16" height="14" fill="none" stroke="#fff" stroke-width="2"/><path d="M2 8h16" stroke="#fff" stroke-width="2"/></svg>15 July,2017</span>
    </div>
  </div>
  <div class="card side" style="left:801px;background:linear-gradient(135deg,#cfd3d8,#6b7a8c 60%,#3d4a5a)" role="img" aria-label="Photo of people working on laptops"></div>
</section>

<section class="testi">
  <h2 class="title">Client <span>Testimonial</span></h2>
  <div class="avatar" role="img" aria-label="Client portrait"></div>
  <p>Lorem Ipsum is simply dummy text of the printing and typesetting industry. Lorem Ipsum has been the industry's standard dummy text ever since the 1500s, when an unknown printer took a galley of type and scrambled it to make a type specimen book.</p>
  <div class="who">~ Client Name</div>
  <div class="dots"><i></i><i class="on"></i><i></i><i></i><i></i></div>
</section>

<section class="contact">
  <h2 class="title">Contact <span>Us</span></h2>
  <div class="field on" style="left:226px;top:134px">Name*</div>
  <div class="field" style="left:613px;top:134px">E-mail*</div>
  <div class="field" style="left:226px;top:187px">Phone*</div>
  <div class="field" style="left:613px;top:187px">Subject*</div>
  <div class="field" style="left:226px;top:240px;width:751px;height:70px">Message</div>
  <div class="btn">Submit Now</div>
</section>

<footer>
  <h5 style="left:80px">Site Map</h5>
  <div class="link" style="top:84px">Home</div>
  <div class="link" style="top:126px">About Us</div>
  <div class="link" style="top:168px">Contact Us</div>

  <h5 style="left:349px">Get In Touch</h5>
  <div class="contact-line" style="top:80px">
    <svg width="16" height="20" viewBox="0 0 16 20"><path d="M8 0a7 7 0 0 1 7 7c0 5-7 13-7 13S1 12 1 7a7 7 0 0 1 7-7z" fill="#f7931e"/><circle cx="8" cy="7" r="2.5" fill="#1e6fbf"/></svg>
    <span>123, Address, State Name,<br>City Name, Zipcode.</span>
  </div>
  <div class="contact-line" style="top:150px">
    <svg width="16" height="16" viewBox="0 0 24 24" fill="#f7931e"><path d="M6.6 10.8a15 15 0 0 0 6.6 6.6l2.2-2.2c.3-.3.7-.4 1-.2 1.1.4 2.3.6 3.6.6.6 0 1 .4 1 1V20c0 .6-.4 1-1 1A17 17 0 0 1 3 4c0-.6.4-1 1-1h3.5c.6 0 1 .4 1 1 0 1.3.2 2.5.6 3.6.1.3 0 .7-.2 1z"/></svg>
    <span>123-456-7890</span>
  </div>
  <div class="contact-line" style="top:193px">
    <svg width="18" height="14" viewBox="0 0 18 14"><rect x="0.5" y="0.5" width="17" height="13" fill="#f7931e"/><path d="M1 1l8 6 8-6" stroke="#1e6fbf" stroke-width="1.4" fill="none"/></svg>
    <span>info@zorvelanalytics.com</span>
  </div>

  <h5 style="left:619px">Newsletter</h5>
  <div class="abs" style="left:619px;top:80px;line-height:26px">For latest news or updates<br>subscribe our newsletter</div>
  <div class="abs" style="left:619px;top:163px;width:232px;height:34px;border-bottom:1px solid rgba(255,255,255,.6)">E-mail*
    <svg class="abs" style="right:8px;top:0" width="18" height="18" viewBox="0 0 24 24"><path d="M2 11L22 2l-9 20-2-9z" fill="#f7931e"/></svg>
  </div>

  <div class="fbrand">Zorvel Analytics</div>
  <div class="abs" style="left:902px;top:140px;width:220px;text-align:center;line-height:26px">Lorem ipsum is simply dummy<br>text of typesetting and printing</div>

  <div class="rule"></div>
  <div class="copy"><span>© Zorvel Analytics- 2018.</span> All Rights Reserved.</div>
  <div class="social" style="left:1040px;top:275px;color:#fff"><i></i><i style="opacity:.6"></i><i style="opacity:.6"></i></div>
</footer>

</body>
</html>
```